Larchfield Medical Rooms - Websit, online payment facility and patient information portal

We are a small specialist medical centre inNewcastle NSW, Australia. We would like a modern, open easy to navigate (we have many elderly clients) webpage for our customers to use. We would like a page for content uploads (like referrals etc), an enquiry page, and some patient information pages.

Our logo is attached. We would like a modern, grey scale or black and white website for our customers to use. The landing page should have high resolution images and use san serif font.

Target Market(s)

General Audience, Modern

Industry/Entity Type

Health And Wellness

Coding

Coded - Design and coding required

Number of Pages Required

5+ page

Font styles to use
Sans Serif

Colors
cbcbcb
757575
7f7f7f
c4c4c4
85cae6
cee9f5
cfdfed

Requirements
Must have
• Landing Page
• Several Other pages for content upload
• Ability to do online payments
• Enquiry form
• Contact page
• Social Media Links

```html
<!DOCTYPE html>
<html lang="en">
<head>
<meta charset="utf-8">
<title>Larchfield Medical Rooms</title>
<link href="https://fonts.googleapis.com/css2?family=Montserrat:wght@300;400;500&family=Lato:wght@400;700&display=swap" rel="stylesheet">
<style>
:root{
  --blue:#85cae6;
  --blue-deep:#5fb2d9;
  --blue-pale:#cee9f5;
  --bar:#cfdfed;
  --ink:#4a4a4a;
  --grey:#757575;
  --grey-mid:#7f7f7f;
  --line:#cbcbcb;
  --line-soft:#e3e3e3;
  --panel:#f4f4f4;
  --white:#ffffff;
}
*{box-sizing:border-box;margin:0;padding:0}
html,body{width:1200px;height:2632px;overflow:hidden;background:var(--white)}
body{position:relative;font-family:"Lato",sans-serif;color:var(--ink)}
.abs{position:absolute}
.heading{font-family:"Montserrat",sans-serif;font-weight:300;color:#555;text-align:center;letter-spacing:1px}

/* header */
.brand{left:98px;top:22px;width:170px;text-align:center;font-family:"Montserrat",sans-serif;font-weight:400;color:#555}
.brand-mark{display:block;margin:0 auto 6px;width:18px;height:18px;border-radius:50%;background:#555}
.brand-name{font-size:25px;letter-spacing:0;line-height:1}
.brand-sub{font-size:12px;letter-spacing:3px;line-height:1.4}
.call{left:526px;top:50px;display:flex;align-items:center;gap:10px}
.call-label{font-size:11px;color:var(--grey);letter-spacing:.5px;font-family:"Montserrat",sans-serif}
.call-number{font-size:23px;color:var(--blue-deep);font-family:"Montserrat",sans-serif;font-weight:300;line-height:1}
.search{left:758px;top:54px;width:344px;height:34px;border:1px solid var(--line);font-size:13px;color:var(--grey);padding:9px 12px;font-family:"Montserrat",sans-serif}
.search svg{position:absolute;right:12px;top:11px}

.nav{left:0;top:125px;width:1200px;height:45px;background:#f1f1f1;border-top:1px solid var(--line-soft);border-bottom:1px solid var(--line-soft)}
.nav ul{position:absolute;left:98px;top:0;display:flex;list-style:none;height:44px}
.nav li{font-family:"Montserrat",sans-serif;font-size:14px;color:#555;padding:0 21px;line-height:44px;border-right:1px solid var(--line-soft)}
.nav li:first-child{border-left:1px solid var(--line-soft)}
.nav li.active{background:var(--blue);color:var(--white)}

/* hero */
.hero{left:0;top:170px;width:1200px;height:580px;background:linear-gradient(100deg,#d9d9d9 0%,#bfbfbf 35%,#e4e4e4 65%,#f2f2f2 100%)}
.hero-curve{left:0;top:170px}
.hero-title{left:0;top:288px;width:1200px;text-align:center;font-family:"Montserrat",sans-serif;font-weight:300;font-size:58px;color:var(--white)}
.enquiry{left:189px;top:381px;width:821px;height:136px;background:rgba(255,255,255,.85);display:flex;gap:16px;padding:48px 36px 0}
.field{width:182px;height:38px;border:1px solid var(--line);background:var(--white);font-size:14px;color:var(--grey-mid);padding:10px 14px;font-family:"Montserrat",sans-serif}
.send{width:148px;height:38px;background:var(--blue);color:var(--white);font-family:"Montserrat",sans-serif;font-weight:500;font-size:17px;text-align:center;line-height:38px;letter-spacing:.5px}
.slide-arrow{top:398px;width:46px;height:46px;border-radius:50%;background:rgba(120,120,120,.35)}

/* welcome */
.welcome-title{left:0;top:726px;width:1200px;font-size:34px}
.welcome-lead{left:0;top:780px;width:1200px;text-align:center;font-size:19px;color:var(--grey)}
.rule{left:98px;top:826px;width:1004px;height:1px;background:var(--line-soft)}
.feature{top:864px;width:320px;text-align:center}
.feature-icon{display:block;margin:0 auto}
.feature-title{margin-top:20px;font-family:"Montserrat",sans-serif;font-weight:500;font-size:20px;color:#444;letter-spacing:.5px}
.feature-text{margin-top:10px;font-size:15px;line-height:21px;color:var(--grey)}
.btn-outline{display:inline-block;border:2px solid var(--blue-pale);color:var(--blue-deep);font-family:"Montserrat",sans-serif;font-size:15px;text-align:center}
.feature .btn-outline{margin-top:18px;width:130px;height:38px;line-height:34px}

/* services */
.services{left:0;top:1214px;width:1200px;height:624px;background:var(--panel)}
.services-title{left:0;top:1260px;width:1200px;font-size:34px}
.card{top:1340px;width:233px;height:347px;background:var(--white)}
.card-photo{height:179px}
.card-title{margin:18px 18px 0;font-family:"Montserrat",sans-serif;font-size:18px;color:#444}
.card-text{margin:10px 18px 0;font-size:13px;line-height:23px;color:var(--grey)}
.view-more{left:519px;top:1742px;width:162px;height:40px;line-height:36px;font-size:17px;background:var(--white)}

/* testimonials */
.clients-title{left:0;top:1898px;width:1200px;font-size:34px}
.clients-rule{left:503px;top:1949px;width:194px;height:1px;background:var(--line)}
.quote{left:215px;top:1982px;width:770px;text-align:center;font-size:16px;line-height:22px;color:var(--grey)}
.quote-mark{font-family:"Montserrat",sans-serif;font-size:64px;color:#cfcfcf;line-height:1}
.avatar{left:558px;top:2066px;width:84px;height:84px;border-radius:50%;border:4px solid var(--white);box-shadow:0 0 0 1px var(--line);background:linear-gradient(160deg,#9fc3dc,#6e9bbb 60%,#dce6ee)}
.client-name{left:0;top:2162px;width:1200px;text-align:center;font-family:"Montserrat",sans-serif;font-weight:500;font-size:15px;color:var(--blue-deep);letter-spacing:.5px}
.dots{left:570px;top:2211px;display:flex;gap:6px}
.dots i{width:11px;height:11px;border-radius:50%;background:var(--blue-deep);display:block}
.dots i.off{background:none;border:1.5px solid var(--blue-deep)}

/* footer */
.footer{left:0;top:2284px;width:1200px;height:286px;background:var(--panel);border-top:1px solid var(--line-soft)}
.footer-brand{left:98px;top:2320px;width:212px;text-align:center;font-family:"Montserrat",sans-serif;color:#222}
.footer-brand .brand-mark{width:26px;height:26px;background:#222;margin-bottom:10px}
.footer-brand .brand-name{font-size:31px}
.footer-brand .brand-sub{font-size:15px;letter-spacing:5px}
.disclaimer{left:98px;top:2476px;width:312px;font-size:11px;line-height:18px;color:#444}
.footer-col{top:2334px}
.footer-col h4{font-family:"Montserrat",sans-serif;font-weight:500;font-size:14px;color:#333;margin-bottom:12px}
.footer-col ul{list-style:none}
.footer-col li{font-size:11px;line-height:27px;color:#444}
.contact-line{display:flex;align-items:center;gap:8px}

.bottom-bar{left:0;top:2570px;width:1200px;height:62px;background:var(--bar)}
.copyright{left:98px;top:2593px;font-size:12px;color:#333}
.social{left:777px;top:2592px;display:flex;align-items:center;gap:14px;font-size:12px;color:#333}
.social i{width:12px;height:12px;border-radius:50%;background:#333;display:block}
</style>
</head>
<body>

<header>
  <div class="abs brand">
    <span class="brand-mark"></span>
    <div class="brand-name">LARCHFIELD</div>
    <div class="brand-sub">Medical Rooms</div>
  </div>

  <div class="abs call">
    <svg width="40" height="40" viewBox="0 0 40 40" aria-hidden="true">
      <circle cx="20" cy="20" r="18" fill="none" stroke="#5fb2d9" stroke-width="2"/>
      <path d="M14 11c1.5-1 2.5-.5 3.2 1l1.3 3c.4 1-.2 1.8-1 2.4l-1 .8c.9 2.3 2.7 4.3 5 5.4l.9-1c.7-.8 1.5-1.2 2.5-.7l2.9 1.5c1.4.7 1.7 1.8.8 3.1-1.4 2-3.6 2.6-6 1.6-5.1-2.2-8.7-6.2-10.2-11.3-.6-2.2.1-4.5 1.6-5.8z" fill="#5fb2d9"/>
    </svg>
    <div>
      <div class="call-label">CALL US TODAY:</div>
      <div class="call-number">012.555.0147</div>
    </div>
  </div>

  <div class="abs search">Search entire here
    <svg width="13" height="13" viewBox="0 0 13 13" aria-hidden="true"><circle cx="5.5" cy="5.5" r="4" fill="none" stroke="#5fb2d9" stroke-width="1.6"/><path d="M8.5 8.5l3.5 3.5" stroke="#5fb2d9" stroke-width="1.6"/></svg>
  </div>

  <nav class="abs nav">
    <ul>
      <li class="active">HOME</li>
      <li>ABOUT US</li>
      <li>OUR LOCATION</li>
      <li>SERVICES</li>
      <li>PATIENTS &amp; GUESTS</li>
      <li>HOW TO HELP</li>
      <li>CAREERS</li>
      <li>CONTACT US</li>
    </ul>
  </nav>
</header>

<section>
  <div class="abs hero" role="img" aria-label="Greyscale photograph of a doctor at a desk writing on a clipboard with a patient"></div>
  <svg class="abs hero-curve" width="1200" height="580" viewBox="0 0 1200 580" aria-hidden="true">
    <path d="M0 580 Q600 380 1200 580 Z" fill="#ffffff"/>
  </svg>
  <div class="abs slide-arrow" style="left:26px"></div>
  <div class="abs slide-arrow" style="left:1117px"></div>
  <svg class="abs" style="left:40px;top:410px" width="20" height="22" viewBox="0 0 20 22" aria-hidden="true"><path d="M13 2L5 11l8 9" fill="none" stroke="#fff" stroke-width="1.5"/></svg>
  <svg class="abs" style="left:1131px;top:410px" width="20" height="22" viewBox="0 0 20 22" aria-hidden="true"><path d="M7 2l8 9-8 9" fill="none" stroke="#fff" stroke-width="1.5"/></svg>

  <h1 class="abs hero-title">Have a Enquiry</h1>
  <form class="abs enquiry">
    <div class="field">Your Name</div>
    <div class="field">Phone number</div>
    <div class="field">Email address</div>
    <div class="send">SEND NOW !</div>
  </form>
</section>

<section>
  <h2 class="abs heading welcome-title">WELCOME TO LARCHFIELD MEDICAL ROOMS</h2>
  <p class="abs welcome-lead">We are a small specialist medical centre in Newcastle NSW, Australia. We have many elderly clients</p>
  <div class="abs rule"></div>

  <div class="abs feature" style="left:89px">
    <svg class="feature-icon" width="150" height="150" viewBox="0 0 150 150" aria-hidden="true">
      <circle cx="75" cy="75" r="74" fill="#85cae6"/><circle cx="75" cy="75" r="67" fill="none" stroke="#fff" stroke-width="2.5"/>
      <path d="M75 40L42 68h8v35h50V68h8z" fill="#fff"/>
      <path d="M70 68h10v10h10v10H80v10H70V88H60V78h10z" fill="#85cae6"/>
    </svg>
    <div class="feature-title">RESIDENTIAL CARE</div>
    <p class="feature-text">Excepteur sint occaecat cupidatat non proident,<br>sunt in culpa qui officia deserunt mollit..</p>
    <span class="btn-outline">READ MORE</span>
  </div>

  <div class="abs feature" style="left:440px">
    <svg class="feature-icon" width="150" height="150" viewBox="0 0 150 150" aria-hidden="true">
      <circle cx="75" cy="75" r="74" fill="#85cae6"/><circle cx="75" cy="75" r="67" fill="none" stroke="#fff" stroke-width="2.5"/>
      <circle cx="75" cy="56" r="14" fill="#fff"/>
      <path d="M46 104c0-17 12-28 29-28s29 11 29 28z" fill="#fff"/>
      <path d="M88 92h4v4h4v4h-4v4h-4v-4h-4v-4h4z" fill="#85cae6"/>
    </svg>
    <div class="feature-title">MEDICAL SPECIALIST</div>
    <p class="feature-text">Excepteur sint occaecat cupidatat non proident,<br>sunt in culpa qui officia deserunt mollit..</p>
    <span class="btn-outline">READ MORE</span>
  </div>

  <div class="abs feature" style="left:789px">
    <svg class="feature-icon" width="150" height="150" viewBox="0 0 150 150" aria-hidden="true">
      <circle cx="75" cy="75" r="74" fill="#85cae6"/><circle cx="75" cy="75" r="67" fill="none" stroke="#fff" stroke-width="2.5"/>
      <path d="M64 46h22v8h-4v-4H68v4h-4z" fill="#fff"/>
      <rect x="42" y="54" width="66" height="48" rx="8" fill="#fff"/>
      <circle cx="75" cy="78" r="16" fill="#85cae6"/>
      <path d="M71 68h8v6h6v8h-6v6h-8v-6h-6v-8h6z" fill="#fff"/>
    </svg>
    <div class="feature-title">LARCHFIELD MEDICINE</div>
    <p class="feature-text">Excepteur sint occaecat cupidatat non proident,<br>sunt in culpa qui officia deserunt mollit..</p>
    <span class="btn-outline">READ MORE</span>
  </div>
</section>

<section>
  <div class="abs services"></div>
  <h2 class="abs heading services-title">OUR SERVICES</h2>

  <article class="abs card" style="left:100px">
    <div class="card-photo" role="img" aria-label="Photograph of a carer helping an elderly woman at home" style="background:linear-gradient(135deg,#b7a79a,#d9cfc6 55%,#8d8f8a)"></div>
    <h3 class="card-title">HOME HEALTH CARE</h3>
    <p class="card-text">Sed do eiusmod tempor incididunt ut labore et dolore magna aliqua quis nostrud exercitation ullamco laboris nisi ut aliqui.</p>
  </article>

  <article class="abs card" style="left:356px">
    <div class="card-photo" role="img" aria-label="Photograph of a young girl resting in bed" style="background:linear-gradient(135deg,#efe7e0,#d9c2b0 50%,#f4f0ec)"></div>
    <h3 class="card-title">PEDIATRIC CARE</h3>
    <p class="card-text">Ut enim ad minima veniam, quis nostrum exercitationem ullam corporis suscipit laboriosam, nisi ut aliquid ex ea commodi.</p>
  </article>

  <article class="abs card" style="left:612px">
    <div class="card-photo" role="img" aria-label="Photograph of a companion reading with an elderly woman" style="background:linear-gradient(135deg,#6b5a55,#d8c8bd 50%,#8a2b35)"></div>
    <h3 class="card-title">COMPANION CARE</h3>
    <p class="card-text">But I must explain to you how all this mistaken idea of denouncing pleasure and praising pain was born and I will give you.</p>
  </article>

  <article class="abs card" style="left:868px">
    <div class="card-photo" role="img" aria-label="Photograph of an elderly couple outdoors at sunset" style="background:linear-gradient(160deg,#f7e6c8,#f0b868 55%,#b9782f)"></div>
    <h3 class="card-title">CONDITIONS TREATED</h3>
    <p class="card-text">At vero eos et accusamus et iusto odio dignissimos ducimus qui blanditiis praesentium voluptatum deleniti atque.</p>
  </article>

  <span class="abs btn-outline view-more">VIEW MORE</span>
</section>

<section>
  <h2 class="abs heading clients-title">WHAT OUR CLIENTS ARE SAYING</h2>
  <div class="abs clients-rule"></div>
  <span class="abs quote-mark" style="left:170px;top:1966px">&ldquo;</span>
  <p class="abs quote">At vero eos et accusamus et iusto odio dignissimos ducimus qui blanditiis praesentium voluptatum deleniti atque corrupti quos dolores et quas molestias excepturi sint occaecati cupiditate non provident, similique sunt in culpa qui officia deserunt mollitia animi, id est laborum et dolorum fuga. Et harum quidem rerum facilis est et expedita distinctio.</p>
  <span class="abs quote-mark" style="left:975px;top:2010px">&rdquo;</span>
  <div class="abs avatar" role="img" aria-label="Portrait photograph of the client"></div>
  <div class="abs client-name">NEWCASTLE NSW - MEDICAL WOMEN</div>
  <div class="abs dots"><i class="off"></i><i></i><i></i></div>
</section>

<footer>
  <div class="abs footer"></div>
  <div class="abs footer-brand">
    <span class="brand-mark"></span>
    <div class="brand-name">LARCHFIELD</div>
    <div class="brand-sub">Medical Rooms</div>
  </div>
  <p class="abs disclaimer">The information found on this site should not be used to diagnose or treat a medical condition. Links to other Internet sites are provided as a convenience.</p>

  <div class="abs footer-col" style="left:460px">
    <h4>COMPANY</h4>
    <ul><li>Medical Check up</li><li>Medical Care</li><li>Health Care</li><li>Mental Health</li><li>Neurology</li><li>Orthopaedics</li></ul>
  </div>
  <div class="abs footer-col" style="left:624px">
    <h4>SERVICES</h4>
    <ul><li>Health Care</li><li>Pediatric Care</li><li>Medical Care</li><li>Companion Care</li><li>Conditions Treated</li><li>More Services</li></ul>
  </div>
  <div class="abs footer-col" style="left:805px">
    <h4>WHY US</h4>
    <ul><li>Medical Centre</li><li>Medical Room</li><li>News</li><li>Site Map</li><li>Vendors</li></ul>
  </div>
  <div class="abs footer-col" style="left:958px">
    <h4>CONTACT INFO</h4>
    <ul>
      <li>Larchfield Medical Rooms</li>
      <li style="line-height:20px;margin-top:4px">Street Address, City Name<br>Newcastle NSW, Australia</li>
      <li class="contact-line" style="margin-top:6px">
        <svg width="11" height="11" viewBox="0 0 40 40" aria-hidden="true"><path d="M8 3c3-2 5-1 6.5 2l2.5 6c.8 2-.4 3.6-2 4.8l-2 1.6c1.8 4.6 5.4 8.6 10 10.8l1.8-2c1.4-1.6 3-2.4 5-1.4l5.8 3c2.8 1.4 3.4 3.6 1.6 6.2-2.8 4-7.2 5.2-12 3.2C15 35 7.8 27 4.8 16.8 3.6 12.4 5 7.8 8 3z" fill="#333"/></svg>
        012.555.0147
      </li>
      <li class="contact-line">
        <svg width="12" height="10" viewBox="0 0 12 10" aria-hidden="true"><rect width="12" height="10" fill="#333"/><path d="M0 0l6 5 6-5" fill="none" stroke="#f4f4f4" stroke-width="1"/></svg>
        hello@larchfieldrooms.example
      </li>
    </ul>
  </div>

  <div class="abs bottom-bar"></div>
  <p class="abs copyright">&copy; 2017. Larchfield Medical Rooms . All rights reserved</p>
  <div class="abs social">Connect with our social network :<i></i><i></i><i></i><i></i><i></i></div>
</footer>

</body>
</html>
```